we do all sorts of cleaning however bookings are limited!
why not chose the right cleaners for you!
pressure cleaning, window cleaning, office, end of lease clean, accommodation, industrial and commercial cleaning and house cleaning

Logo Text

Bright Nest Cleaning Service

```html
<!DOCTYPE html>
<html lang="en">
<head>
<meta charset="utf-8">
<title>Bright Nest Cleaning Service – Business Cards</title>
<link rel="stylesheet" href="https://fonts.googleapis.com/css2?family=Open+Sans:wght@400;600;700;800&display=swap">
<style>
  :root {
    --stage: #2b2b2b;
    --white: #ffffff;
    --brand-blue: #0a9be3;
    --brand-blue-deep: #0390e4;
    --brand-blue-light: #00b1f2;
    --leaf-green: #7cc242;
    --ink: #333333;
    --ink-soft: #555555;
    --rule: #6b6b6b;
    --splash-pale: #d6eefb;
  }
  * { box-sizing: border-box; margin: 0; padding: 0; }
  html, body {
    width: 1200px; height: 900px; overflow: hidden;
    background: var(--stage);
    font-family: "Open Sans", Arial, sans-serif;
  }
  .stage {
    position: relative; width: 1200px; height: 900px;
    display: flex; flex-direction: column; align-items: center; justify-content: center; gap: 40px;
  }
  .card {
    position: relative; width: 640px; height: 366px; border-radius: 28px; overflow: hidden;
  }

  /* Front card */
  .card--front { background: var(--white); color: var(--ink); }
  .card--front .brand-name {
    position: absolute; top: 42px; left: 0; right: 0; text-align: center;
    font-size: 40px; font-weight: 800; line-height: 1.1; color: var(--brand-blue);
  }
  .card--front .splash {
    position: absolute; right: -30px; bottom: -20px; width: 170px; height: 200px;
    border-radius: 60% 40% 50% 50%;
    background: radial-gradient(circle at 40% 40%, var(--splash-pale), rgba(214,238,251,0.2));
  }
  .contact-row {
    position: absolute; left: 44px; right: 44px; top: 170px;
    display: flex; align-items: stretch; gap: 34px;
  }
  .contact-person, .contact-company { display: flex; flex-direction: column; gap: 6px; }
  .contact-person { width: 230px; }
  .divider { width: 1px; background: var(--rule); }
  .person-name { font-size: 20px; font-weight: 600; color: var(--brand-blue); letter-spacing: .2px; }
  .person-role { font-size: 14px; color: var(--ink-soft); margin-bottom: 8px; }
  .company-name { font-size: 16px; font-weight: 700; color: var(--brand-blue); }
  .address { font-size: 15px; line-height: 1.35; color: var(--ink); }
  .line { display: flex; align-items: center; gap: 9px; font-size: 15px; color: var(--ink); }
  .line svg { flex: none; }

  /* Back card */
  .card--back {
    background: linear-gradient(135deg, var(--brand-blue-deep), var(--brand-blue-light) 60%, var(--brand-blue-deep));
    color: var(--white);
  }
  .card--back .brand-name {
    position: absolute; top: 46px; left: 0; right: 0; text-align: center;
    font-size: 40px; font-weight: 800; line-height: 1.1; color: var(--white);
  }
  .card--back .splash {
    position: absolute; right: -40px; top: 110px; width: 130px; height: 200px;
    border-radius: 55% 45% 50% 50%;
    background: radial-gradient(circle at 40% 50%, rgba(255,255,255,0.16), rgba(255,255,255,0.03));
  }
  .service-list {
    position: absolute; left: 30px; right: 30px; bottom: 40px;
    display: flex; justify-content: space-between; list-style: none;
  }
  .service {
    width: 90px; display: flex; flex-direction: column; align-items: center; gap: 10px; text-align: center;
  }
  .service-icon {
    width: 54px; height: 54px; border-radius: 10px;
    border: 2px solid rgba(255,255,255,0.85); background: rgba(255,255,255,0.12);
  }
  .service-label { font-size: 13px; line-height: 1.25; }
</style>
</head>
<body>
<main class="stage">

  <section class="card card--front">
    <h1 class="brand-name">Bright Nest<br>Cleaning Service</h1>
    <div class="splash" role="img" aria-label="Soft pale blue water splash decoration"></div>
    <div class="contact-row">
      <div class="contact-person">
        <p class="person-name">YOUR NAME HERE</p>
        <p class="person-role">Designation Here</p>
        <p class="line">
          <svg width="18" height="18" viewBox="0 0 18 18" aria-hidden="true"><circle cx="9" cy="9" r="9" fill="#7cc242"/><path d="M6 4.5c.6 3.6 3.3 6.6 7 7.3l.5-1.8-2-1-1 .9c-1.2-.6-2.2-1.6-2.8-2.8l.9-1-1-2z" fill="#fff"/></svg>
          +41 00 000 00 00
        </p>
        <p class="line">
          <svg width="18" height="18" viewBox="0 0 18 18" aria-hidden="true"><circle cx="9" cy="9" r="9" fill="#7cc242"/><rect x="4.5" y="6" width="9" height="6.5" rx="1" fill="#fff"/><path d="M4.8 6.3 9 9.6l4.2-3.3" stroke="#7cc242" fill="none" stroke-width="1"/></svg>
          info@brightnestclean.com
        </p>
      </div>
      <span class="divider" aria-hidden="true"></span>
      <div class="contact-company">
        <p class="company-name">BRIGHT NEST CLEANING SERVICE</p>
        <p class="address">123 Street Name,<br>City Name 000 123</p>
        <p class="line">
          <svg width="18" height="18" viewBox="0 0 18 18" aria-hidden="true"><circle cx="9" cy="9" r="9" fill="#7cc242"/><g stroke="#fff" fill="none" stroke-width="1"><circle cx="9" cy="9" r="4.8"/><ellipse cx="9" cy="9" rx="2" ry="4.8"/><path d="M4.2 9h9.6"/></g></svg>
          www.brightnestclean.com
        </p>
      </div>
    </div>
  </section>

  <section class="card card--back">
    <h2 class="brand-name">Bright Nest<br>Cleaning Service</h2>
    <div class="splash" role="img" aria-label="Faint white water splash decoration"></div>
    <ul class="service-list">
      <li class="service"><span class="service-icon" role="img" aria-label="Pressure washer icon"></span><span class="service-label">Pressure Cleaning</span></li>
      <li class="service"><span class="service-icon" role="img" aria-label="Window wiping icon"></span><span class="service-label">Window Cleaning</span></li>
      <li class="service"><span class="service-icon" role="img" aria-label="Office desk icon"></span><span class="service-label">Office Cleaning</span></li>
      <li class="service"><span class="service-icon" role="img" aria-label="House with checklist icon"></span><span class="service-label">End Of Lease Clean</span></li>
      <li class="service"><span class="service-icon" role="img" aria-label="Industrial building icon"></span><span class="service-label">Industrial &amp; Commercial Cleaning</span></li>
      <li class="service"><span class="service-icon" role="img" aria-label="House with brush icon"></span><span class="service-label">House Cleaning</span></li>
    </ul>
  </section>

</main>
</body>
</html>
```